Smile club flyer design

I am launching an office smile club and would like a design that sits my branding and that is appealing to customers. I have a design (I need a new one) that has all the information.
My website is maplecrestdentalcaretn.example
Brand color is green. The design can be any color

Target Market(s)

Ages 30+

Industry/Entity Type

Dental

Font styles to use
Serif

Requirements
Must have
• Appealing to patients

```html
<!DOCTYPE html>
<html lang="en">
<head>
<meta charset="utf-8">
<title>Maplecrest Dental Care – Smile Club Membership</title>
<link href="https://fonts.googleapis.com/css2?family=Marcellus&family=Poppins:wght@400;500;600;700;800&display=swap" rel="stylesheet">
<style>
  :root{
    --backdrop:#082822;
    --teal:#17b8a6;
    --teal-deep:#12a493;
    --mint:#bdeee6;
    --mint-pale:#e3f8f4;
    --ink:#16212e;
    --white:#ffffff;
    --magenta:#c8237f;
    --text:#1d2a30;
  }
  *{margin:0;padding:0;box-sizing:border-box}
  html,body{width:1200px;height:1200px;overflow:hidden;background:var(--backdrop)}
  body{font-family:"Poppins",sans-serif;color:var(--text);position:relative}
  .flyer{position:absolute;left:245px;top:98px;width:709px;height:1003px;
    background:linear-gradient(180deg,var(--mint) 0%,var(--mint-pale) 75%,var(--mint) 100%);
    box-shadow:0 10px 40px rgba(0,0,0,.45);overflow:hidden}
  .header{position:absolute;left:0;top:0;width:100%;height:317px;background:var(--teal)}
  .decor{position:absolute;border-radius:50%;pointer-events:none}
  .decor--tl{left:-60px;top:-40px;width:200px;height:260px;background:radial-gradient(circle,rgba(255,255,255,.16),rgba(255,255,255,0) 70%)}
  .decor--tr{right:-60px;top:-40px;width:200px;height:260px;background:radial-gradient(circle,rgba(255,255,255,.16),rgba(255,255,255,0) 70%)}
  .decor--bl{left:-60px;bottom:-60px;width:220px;height:220px;background:radial-gradient(circle,rgba(23,184,166,.18),rgba(23,184,166,0) 70%)}
  .decor--br{right:-60px;bottom:-60px;width:220px;height:220px;background:radial-gradient(circle,rgba(23,184,166,.18),rgba(23,184,166,0) 70%)}
  .brand{position:absolute;top:38px;width:100%;text-align:center;color:var(--white)}
  .brand__name{font-family:"Marcellus",serif;font-size:44px;line-height:1;letter-spacing:-.5px}
  .brand__sub{font-family:"Poppins",sans-serif;font-weight:600;font-size:15px;letter-spacing:6px;margin-top:6px}
  .brand__sub::before,.brand__sub::after{content:"";display:inline-block;width:24px;height:2px;background:var(--white);vertical-align:middle;margin:0 8px}
  .intro{position:absolute;top:148px;width:100%;text-align:center;color:var(--white);font-weight:700;font-size:15px;letter-spacing:5px}
  .title{position:absolute;top:168px;width:100%;text-align:center;color:var(--white);font-family:"Marcellus",serif;font-size:86px;line-height:1}
  .subtitle{position:absolute;top:254px;width:100%;text-align:center;color:var(--white);font-family:"Marcellus",serif;font-size:40px;letter-spacing:4px;line-height:1}
  .pill{position:absolute;top:304px;height:27px;border:1px solid var(--teal);border-radius:14px;background:var(--white);
    color:var(--teal);font-weight:600;font-size:15px;display:flex;align-items:center;justify-content:center}
  .pill--left{left:121px;width:236px}
  .pill--right{left:368px;width:228px}
  .plan{position:absolute;width:306px;border:1px solid var(--teal);border-radius:20px;background:rgba(255,255,255,.18)}
  .plan--core{left:37px;top:360px;height:171px}
  .plan--bright{left:366px;top:360px;height:171px}
  .plan--perio{left:37px;top:551px;height:179px}
  .plan--refresh{left:366px;top:551px;height:179px}
  .plan__bar{position:absolute;left:6px;right:5px;top:6px;height:50px;background:var(--teal);border-radius:25px}
  .plan__name{position:absolute;left:21px;top:9px;color:var(--white);font-weight:600;font-size:17px;line-height:17px}
  .plan__price{position:absolute;right:0;top:7px;height:36px;background:var(--ink);border-radius:18px;color:var(--white);
    font-weight:600;font-size:23px;display:flex;align-items:center;padding:0 12px 0 16px}
  .plan__price small{font-size:13px;font-weight:400;color:var(--teal);margin-left:5px}
  .plan__badge{position:absolute;left:5px;top:3px;width:44px;height:44px;border-radius:50%;background:var(--magenta);border:2px solid var(--white);
    color:var(--white);font-weight:800;font-size:13px;display:flex;align-items:center;justify-content:center;transform:rotate(-12deg)}
  .plan__list{position:absolute;left:27px;top:72px;list-style:none;font-size:13px;line-height:15.5px;color:var(--text)}
  .plan__list li{position:relative;padding-left:15px;margin-bottom:5px}
  .plan__list li svg{position:absolute;left:0;top:4px;width:9px;height:9px}
  .plan__list li.plain{padding-left:15px}
  .plan__list li.offer{font-family:"Marcellus",serif;color:var(--teal);font-size:17px;margin-top:4px}
  .plan__list li.offer svg{top:7px}
  .plus{display:inline-block;width:10px;height:10px;border-radius:50%;background:var(--teal);color:var(--white);font-size:10px;line-height:10px;text-align:center;font-weight:700;margin-left:3px;vertical-align:1px}
  .cta{position:absolute;left:46px;top:756px;width:618px;height:48px;background:var(--teal);border-radius:24px;
    display:flex;align-items:center;justify-content:center;font-weight:800;font-size:25px;letter-spacing:2px;color:var(--white)}
  .cta__phone{color:var(--ink);margin-left:10px}
  .financing{position:absolute;top:826px;width:100%;text-align:center;font-weight:600;font-size:14px;letter-spacing:2.5px;color:var(--ink)}
  .partners{position:absolute;top:862px;width:100%;display:flex;justify-content:center;gap:34px;align-items:center}
  .partner{font-weight:700;font-size:26px;color:#3a3a44;display:flex;align-items:center;gap:8px}
  .partner__dot{width:14px;height:14px;border-radius:50%;background:var(--teal)}
  .plans-note{position:absolute;top:912px;width:100%;text-align:center;font-weight:600;font-size:13px;letter-spacing:2.5px;color:var(--teal)}
  .fee{position:absolute;top:952px;width:100%;text-align:center;font-size:10px;letter-spacing:1.2px;color:var(--ink)}
</style>
</head>
<body>
<main class="flyer">
  <div class="header">
    <div class="decor decor--tl" role="img" aria-label="Soft leaf pattern decoration"></div>
    <div class="decor decor--tr" role="img" aria-label="Soft leaf pattern decoration"></div>
    <div class="brand">
      <div class="brand__name">Maplecrest</div>
      <div class="brand__sub">DENTAL CARE</div>
    </div>
    <div class="intro">INTRODUCING</div>
    <h1 class="title">SMILE CLUB</h1>
    <div class="subtitle">MEMBERSHIP</div>
  </div>
  <div class="decor decor--bl" role="img" aria-label="Soft leaf pattern decoration"></div>
  <div class="decor decor--br" role="img" aria-label="Soft leaf pattern decoration"></div>

  <div class="pill pill--left">AFFORDABLE DENTAL CARE</div>
  <div class="pill pill--right">NO INSURANCE REQUIRED</div>

  <svg width="0" height="0" style="position:absolute">
    <defs>
      <symbol id="tick" viewBox="0 0 10 10"><circle cx="5" cy="5" r="4.3" fill="none" stroke="#17b8a6" stroke-width="1"/><path d="M3 5.1l1.4 1.4L7 3.8" fill="none" stroke="#17b8a6" stroke-width="1"/></symbol>
    </defs>
  </svg>

  <section class="plan plan--core">
    <div class="plan__bar">
      <div class="plan__name">CORE CARE<br>PREVENTIVE</div>
      <div class="plan__price">$39<small>/MONTH</small></div>
    </div>
    <ul class="plan__list">
      <li><svg><use href="#tick"/></svg>Comprehensive Annual Exam</li>
      <li><svg><use href="#tick"/></svg>2 Professional Cleanings per Year</li>
      <li><svg><use href="#tick"/></svg>Routine Bitewing X-rays</li>
      <li><svg><use href="#tick"/></svg>10% Savings on Treatment</li>
    </ul>
  </section>

  <section class="plan plan--bright">
    <div class="plan__bar">
      <div class="plan__name">BRIGHT<br>COSMETIC</div>
      <div class="plan__price">$59<small>/MONTH</small></div>
    </div>
    <ul class="plan__list">
      <li><svg><use href="#tick"/></svg>Annual In-Office Whitening<br>(Top &amp; Bottom)</li>
      <li><svg><use href="#tick"/></svg>Custom Whitening Trays</li>
      <li><svg><use href="#tick"/></svg>15% Savings on Elective Treatment</li>
    </ul>
  </section>

  <section class="plan plan--perio">
    <div class="plan__bar">
      <div class="plan__name">TOTAL SMILE<br>PERIODONTAL</div>
      <div class="plan__price">$89<small>/MONTH</small></div>
    </div>
    <ul class="plan__list">
      <li><svg><use href="#tick"/></svg>3-4 Perio Maintenance Visits per Year</li>
      <li><svg><use href="#tick"/></svg>1 Comprehensive Exam</li>
      <li><svg><use href="#tick"/></svg>Diagnostic X-rays</li>
      <li><svg><use href="#tick"/></svg>15% Savings on Restorative &amp;<br>Elective Care</li>
    </ul>
  </section>

  <section class="plan plan--refresh">
    <div class="plan__bar">
      <div class="plan__badge">NEW</div>
      <div class="plan__name" style="left:61px">SMILE REFRESH<br>PACKAGE</div>
      <div class="plan__price" style="font-size:25px">$499</div>
    </div>
    <ul class="plan__list" style="left:30px">
      <li><svg><use href="#tick"/></svg>Cleaning<span class="plus">+</span></li>
      <li class="plain">Comprehensive Exam<span class="plus">+</span></li>
      <li class="plain">Whitening</li>
      <li class="offer"><svg><use href="#tick"/></svg>Limited Time Offer</li>
    </ul>
  </section>

  <div class="cta">JOIN SMILE CLUB TODAY!<span class="cta__phone">865-555-0142</span></div>

  <div class="financing">FLEXIBLE FINANCING FOR TREATMENT</div>
  <div class="partners">
    <div class="partner"><span class="partner__dot"></span>CareLine</div>
    <div class="partner"><span class="partner__dot"></span>Berrypay</div>
  </div>
  <div class="plans-note">PAYMENT PLANS AVAILABLE</div>
  <div class="fee">*$49 Lifetime Activation Fee (Non-Refundable)</div>
</main>
</body>
</html>
```